Investment Company Business Card Design

We need a Business Card design for a new company based in Boston called "Velm Investment". We are cooperating with local real estate and construction companies. Our company is very actively and aggressively acquiring primarily residential investment properties either to buy and hold long term or for purposes or renovating and repositioning for re-sale in the market. In addition, we undertake some development projects and acquisitions as opportunities present themselves. the final design should contains information about “Velm" the river boat. we hold a steady course, keep a firm hand, and let every project sail on a fair wind from harbor to harbor for our partners.
sample Info. on Design:
Tusa Merrick
CEO
555-xxx-xxxx
418 Harlow St. Suite 507, Fenmoor, RI 02111
Please provide a template also, that we can edit the info later.
Reason: i just got new LOGO Design attached will be use in Business Card Design.
Construction

```html
<!DOCTYPE html>
<html lang="en">
<head>
<meta charset="utf-8">
<title>Velm Investment — Business Card</title>
<link rel="stylesheet" href="https://fonts.googleapis.com/css2?family=Questrial&display=swap">
<style>
  :root {
    --page-bg: #ececec;
    --wood-light: #a97b56;
    --wood-mid: #8e5f3e;
    --wood-dark: #7a4d30;
    --wood-flat-top: #a87758;
    --wood-flat-bottom: #9a6a4b;
    --ink: #6a3d22;
    --ink-soft: #7a4a2c;
  }
  * { margin: 0; padding: 0; box-sizing: border-box; }
  html, body {
    width: 1200px;
    height: 720px;
    overflow: hidden;
    background: var(--page-bg);
    font-family: "Questrial", sans-serif;
  }
  .cards {
    position: absolute;
    top: 241px;
    left: 146px;
    display: flex;
    gap: 66px;
  }
  .card {
    position: relative;
    width: 422px;
    height: 240px;
    border-radius: 2px;
    color: var(--ink);
  }
  .card--front {
    background: linear-gradient(160deg, var(--wood-light) 0%, var(--wood-mid) 55%, var(--wood-dark) 100%);
  }
  .card--back {
    background: linear-gradient(180deg, var(--wood-flat-top) 0%, var(--wood-flat-bottom) 100%);
  }
  .brand {
    position: absolute;
    display: flex;
    align-items: center;
    gap: 10px;
    color: var(--ink);
    white-space: nowrap;
  }
  .brand__mark {
    width: 12px;
    height: 12px;
    border-radius: 50%;
    background: var(--ink);
  }
  .brand--front {
    left: 0;
    right: 0;
    top: 92px;
    justify-content: center;
    font-size: 36px;
  }
  .brand--back {
    right: 26px;
    top: 56px;
    font-size: 20px;
  }
  .brand--back .brand__mark { width: 8px; height: 8px; }
  .contact {
    position: absolute;
    left: 12px;
    top: 106px;
    color: var(--ink-soft);
  }
  .contact__name { font-size: 16px; line-height: 20px; }
  .contact__role { font-size: 10px; line-height: 14px; }
  .contact__phone { font-size: 10px; line-height: 14px; margin-top: 42px; }
  .contact__address { font-size: 10px; line-height: 14px; margin-top: 2px; }
  .motto {
    position: absolute;
    right: 14px;
    top: 112px;
    width: 176px;
    font-size: 9.5px;
    line-height: 20px;
    text-align: center;
    color: var(--ink-soft);
  }
</style>
</head>
<body>
  <main class="cards">
    <section class="card card--front" role="img" aria-label="Front of card: wood grain finish with the Velm Investment name">
      <div class="brand brand--front">
        <span class="brand__mark"></span>
        <span class="brand__name">Velm Investment</span>
      </div>
    </section>

    <section class="card card--back" aria-label="Back of card">
      <div class="brand brand--back">
        <span class="brand__mark"></span>
        <span class="brand__name">Velm Investment</span>
      </div>
      <div class="contact">
        <p class="contact__name">Tusa Merrick</p>
        <p class="contact__role">CEO</p>
        <p class="contact__phone">555-xxx-xxxx</p>
        <p class="contact__address">418 Harlow St. Suite 507, Fenmoor, RI</p>
      </div>
      <p class="motto">we hold a steady course, keep a firm hand, and let every project sail on a fair wind from harbor to harbor for our partners.</p>
    </section>
  </main>
</body>
</html>
```